Merrowind Flyer

A simple flyer that gets people attention
I have a attached a sample of what we use now and a picture we use
We service gas fireplaces and need a eye catching but not to cluttered flyer to promote our business. the cost per fireplace should be $60.00

Reason: Sorry for the delay We are out of town on holidays with sketchy internet service To frustrating to complete this project till I am back in a week Thank you for your patience Kind regards Dale

```html
<!DOCTYPE html>
<html lang="en">
<head>
<meta charset="utf-8">
<title>Merrowind Gas Services Flyer</title>
<link rel="stylesheet" href="https://fonts.googleapis.com/css2?family=Open+Sans:ital,wght@0,400;0,600;0,700;1,400;1,600&display=swap">
<style>
:root{
  --stage:#3b3b3b;
  --orange:#e8582a;
  --orange-text:#e4501e;
  --rust:#a8472a;
  --rust-dark:#97401f;
  --ink:#4a4a4a;
  --muted:#666;
  --white:#fff;
  --photo-dark:#2a1a14;
  --photo-warm:#a8582e;
}
*{box-sizing:border-box;margin:0;padding:0}
html,body{width:1200px;height:772px;overflow:hidden}
body{background:var(--stage);font-family:"Open Sans",Arial,sans-serif;position:relative;color:var(--ink)}
.flyer{position:absolute;top:80px;width:475px;height:612px;background:var(--white);overflow:hidden}
.flyer--stacked{left:113px}
.flyer--split{left:635px}
.photo{position:absolute;background:radial-gradient(ellipse at 55% 25%,#d98a3c 0%,var(--photo-warm) 25%,#5a3222 55%,var(--photo-dark) 100%)}
.abs{position:absolute}
.notice-title{color:var(--white);font-weight:700;letter-spacing:.3px}
.property-name{color:var(--white);font-style:italic}
.price-badge{display:flex;align-items:center;color:var(--white)}
.brand-name{font-size:22px;line-height:1;font-weight:600}
.brand-sub{font-size:17px;line-height:1.1}
.price-divider{width:1px;background:rgba(255,255,255,.8);align-self:stretch;margin:0 10px}
.price-at{font-size:14px}
.price{font-size:24px;font-weight:700}
.price-note{font-size:10px;display:block;margin-top:-2px}
.lead{color:var(--orange-text);font-weight:700;text-transform:uppercase;font-size:8.6px;line-height:1.25}
.body-text{color:var(--ink);font-size:8.6px;line-height:1.3;font-weight:600}
.fine-text{color:var(--muted);font-size:6.3px;line-height:1.35;text-align:justify}
.payment-note{color:var(--orange-text);font-style:italic;font-size:6.3px;line-height:1.4}
.signs-heading{color:var(--white);font-weight:700;font-size:7.3px;line-height:1.35;text-transform:uppercase}
.signs-list{list-style:none;color:var(--white);font-size:7.2px;line-height:1.2}
.signs-list li{display:flex;margin-bottom:4px}
.signs-list b{width:18px;flex:none}
.contact-label{color:var(--white);font-style:italic;font-size:7.2px}
.phone{color:var(--white);font-weight:700;font-size:22px;letter-spacing:.5px}
.email{color:var(--white);font-size:7.4px}
.rule{position:absolute;height:1px;background:rgba(255,255,255,.7)}
</style>
</head>
<body>

<!-- Flyer A: stacked layout -->
<article class="flyer flyer--stacked">
  <div class="photo" role="img" aria-label="Photo of a family's bare feet warming in front of a lit fireplace" style="left:0;top:0;width:475px;height:333px"></div>
  <h1 class="notice-title abs" style="top:20px;width:100%;text-align:center;font-size:23px">NOTICE TO THE OWNERS</h1>
  <p class="property-name abs" style="top:55px;width:100%;text-align:center;font-size:17px">NAME OF PROPERTY</p>

  <div class="price-badge abs" style="left:105px;top:260px;width:258px;height:70px;background:var(--orange);padding:0 14px 0 24px">
    <div><div class="brand-name">MERROWIND</div><div class="brand-sub">GAS SERVICES</div></div>
    <span class="price-divider" style="margin:14px 10px"></span>
    <div><span class="price-at">at </span><span class="price">$60</span><span class="price-note">(tax included)</span></div>
  </div>

  <div class="abs" style="left:20px;top:353px;width:260px">
    <p class="lead">Merrowind Gas Services will be on site conducting gas fireplace safety inspections and maintenance for name of property on date of service.</p>
    <p class="body-text" style="margin-top:4px;text-align:justify">If you wish to have your fireplace serviced, please put your name and unit number on the sign-up sheet provided. We will require approximately 20 - 30 minutes to service each fireplace and require that the fireplace is cool to conduct the work.</p>
    <p class="lead" style="margin-top:4px;text-align:justify">Please do not use your fireplace within 2 hours of your appointment as we do not want the technicians to receive burns.</p>
    <p class="fine-text" style="margin-top:6px">The National Home Energy Office states that all fireplaces require regular servicing. Fireplace manufacturers recommend each unit be serviced annually by a qualified technician and insurance companies and Fire Departments are now asking for reports regarding fireplace safety inspections and servicing. The service Merrowind Gas Services will provide will entail a thorough assessment of pilot, burner and valve operation, a door seal inspection, an inspection of the electrical circuits, repositioning of the logs, cleaning and adjustment of fan and controls, cleaning of the firebox and glass, a carbon monoxide test, testing of fittings for gas leaks and a complete operational test once the service is complete.</p>
    <p class="payment-note" style="margin-top:8px">(Owners must have payment ready at time of inspection.<br>Payment may be made in the form of cash, cheque, or credit card)</p>
  </div>

  <aside class="abs" style="left:295px;top:353px;width:180px;height:259px;background:var(--orange);padding:14px 12px">
    <p class="signs-heading">Possible indication that your gas fireplace requires service include:</p>
    <ol class="signs-list" style="margin-top:12px">
      <li><b>(1)</b>Cloudy film on glass</li>
      <li><b>(2)</b>Strong odors when fireplace is in operation</li>
      <li><b>(3)</b>Soot build up on glass, logs or exterior of building</li>
      <li><b>(4)</b>Tarnished/discolored brass</li>
      <li><b>(5)</b>Pilot light outages</li>
      <li><b>(6)</b>Main burner is not lighting consistently</li>
      <li><b>(7)</b>Delayed ignition</li>
      <li><b>(8)</b>Flames are not evenly dispersed.</li>
    </ol>
    <span class="rule" style="left:12px;right:18px;top:182px"></span>
    <p class="contact-label abs" style="left:12px;top:196px">For further information please contact Tessa at:</p>
    <p class="phone abs" style="left:12px;top:208px">604.555.0182</p>
    <p class="email abs" style="left:12px;top:239px">tessa.merrowindgas@mailbox.net</p>
  </aside>
</article>

<!-- Flyer B: split layout -->
<article class="flyer flyer--split">
  <div class="photo" role="img" aria-label="Photo of a family's bare feet warming in front of a lit fireplace" style="left:0;top:0;width:287px;height:315px"></div>
  <div class="price-badge abs" style="left:26px;top:18px">
    <div><div class="brand-name" style="font-size:21px">MERROWIND</div><div class="brand-sub" style="font-size:16px">GAS SERVICES</div></div>
    <span class="price-divider" style="margin:2px 12px"></span>
    <div><span class="price-at">at </span><span class="price">$60</span><span class="price-note">(tax included)</span></div>
  </div>

  <aside class="abs" style="left:287px;top:0;width:188px;height:315px;background:var(--rust);padding:22px 14px 0 16px">
    <h2 class="notice-title" style="font-size:22px;line-height:1.3">NOTICE TO<br>THE OWNERS</h2>
    <p class="property-name" style="font-size:13px;margin-top:6px">NAME OF PROPERTY</p>
    <span class="rule" style="left:16px;right:14px;top:120px"></span>
    <p class="signs-heading" style="margin-top:30px;font-size:7px">Possible indication that your gas fireplace requires service include:</p>
    <ol class="signs-list" style="margin-top:10px;font-size:7px">
      <li><b>(1)</b>Cloudy film on glass</li>
      <li><b>(2)</b>Strong odors when fireplace is in operation</li>
      <li><b>(3)</b>Soot build up on glass, logs or exterior of building</li>
      <li><b>(4)</b>Tarnished/discolored brass</li>
      <li><b>(5)</b>Pilot light outages</li>
      <li><b>(6)</b>Main burner is not lighting consistently</li>
      <li><b>(7)</b>Delayed ignition</li>
      <li><b>(8)</b>Flames are not evenly dispersed.</li>
    </ol>
  </aside>

  <div class="abs" style="left:22px;top:334px;width:440px">
    <p class="lead" style="font-size:9.2px">Merrowind Gas Services will be on site conducting gas fireplace safety inspections and maintenance for name of property on date of service.</p>
    <p class="body-text" style="margin-top:4px;font-size:9px;text-align:justify">If you wish to have your fireplace serviced, please put your name and unit number on the sign-up sheet provided. We will require approximately 20 - 30 minutes to service each fireplace and require that the fireplace is cool to conduct the work.</p>
    <p class="lead" style="margin-top:4px;font-size:9.2px">Please do not use your fireplace within 2 hours of your appointment as we do not want the technicians to receive burns.</p>
  </div>
  <p class="fine-text abs" style="left:22px;top:437px;width:290px">The National Home Energy Office states that all fireplaces require regular servicing. Fireplace manufacturers recommend each unit be serviced annually by a qualified technician and insurance companies and Fire Departments are now asking for reports regarding fireplace safety inspections and servicing. The service Merrowind Gas Services will provide will entail a thorough assessment of pilot, burner and valve operation, a door seal inspection, an inspection of the electrical circuits, repositioning of the logs, cleaning and adjustment of fan and controls, cleaning of the firebox and glass, a carbon monoxide test, testing of fittings for gas leaks and a complete operational test once the service is complete.</p>
  <div class="abs" role="img" aria-label="Illustration of a brick fireplace with a burning fire" style="left:322px;top:436px;width:140px;height:96px;background:linear-gradient(180deg,#c7643a,#a8472a)"></div>

  <footer class="abs" style="left:0;top:535px;width:475px;height:77px;background:var(--rust-dark)">
    <p class="contact-label abs" style="left:20px;top:14px">For further information please contact Tessa at:</p>
    <p class="abs" style="left:20px;top:26px;color:var(--white);font-size:13px">MERROWIND GAS SERVICES</p>
    <p class="phone abs" style="left:20px;top:40px">604.555.0182</p>
    <p class="contact-label abs" style="right:16px;top:20px;font-style:normal;text-align:right">You may also email us at:</p>
    <p class="email abs" style="right:16px;top:32px">tessa.merrowindgas@mailbox.net</p>
    <p class="contact-label abs" style="right:16px;top:46px;text-align:right;font-size:6.4px;line-height:1.35">(Owners must have payment ready at time of inspection.<br>Payment may be made in the form of cash, cheque, or credit card)</p>
  </footer>
</article>

</body>
</html>
```